Create the BEST and COOLEST website for events and media company!

Hi there. I am a start-up events and conferences company with a twist, and we are seeking a highly modern website for our company Quillfern Media. Our company believes that (like the social networking theory) that each and every one of us is connected to anyone on the planet in six connections or less. E.g. I know someone, who knows someone, who knows someone. Hence, the name Quillfern Media.

I have included the copy for the website attached.

While we do have a business audience, they are in the fields of technology from the banking, health, government sector. We would like our website to be edgy, fresh and steer away from stuffy corporate images.

To give you an idea, our website menu tabs will be labelled:
HOME: This will include a corporate video that’s being created next week for me. However, please still design this page with a very striking background image that fills the whole page. You can run the copy and put a mock video for me to just see the layout (we can insert the finished video later).

ROCKSTARS: this will show pictures of highly powerful leaders speaking on stage; with a highly engaged audience watching. We want to show we have the world’s best technology International speakers “rockstars” who are the best in their game when it comes to talking about the future of technology.

LOCAL LEGENDS: like the international ‘rockstar’ speakers we would bring over to Australia to present; this LOCAL LEGENDS page should show we have the best home-grown Chief business people speaking at conferences and smaller powerful roundtable luncheons.

UNSUNG HEROES: this is more the people in the audience who ask questions on a microphone; those that attend the conferences; or a speaking to people at a conference.

THE BAND: this is like an ‘about us’ – just a funkier name to tie in with the theme of rockstars, etc.

THE PARTNERS: this is like a sponsor client page, where we invite people to partner with us and sponsor our events and conferences.

YOU & DORIAN PELLHAM: Dorian Pellham is a famous actor who made the term ‘six degrees of separation’ very popular. This page will have a little bit of an introduction, but mainly have the following video fill the landing page: https://www.vidplume.example/watch?v=Tq4-zLp8XwE

Website Functionality and Features:

• Try and make the ‘vibe’ and look and feel consistent, hip and modern (but still maintain a professional look). At the end of the day, people looking at our website are very senior business chiefs of organisations and also marketing chiefs.
• We may add more pages once we become established, so the website needs to ensure we can do that easily.
• We want pictures to not look stock photos. We want them to fresh, innovative, inspirational.
• Images should have a ‘wow’ factor. Like this one: https://www.picharbor.example/detail/news-photo/general-view-of-atmosphere-during-brightloom-talks-2018-from-me-news-photo/481253907
• Need a mix of speaker, stage, audience, pictures. While we want to be fresh, edgy and contemporary we need to remember our viewers are the big chiefs of businesses – so lets try and have cool shots, but ensure there is a link to the business decision makers in a modern way. They all don’t have to wear suits, but not too casual either
• Other types of imagery I like is this one: https://www.picharbor.example/detail/photo/smiling-audience-using-smart-phone-flashlights-for-royalty-free-image/362817045.
• The following are ok, not wow – but to give you an idea:
• https://www.picharbor.example/detail/photo/smiling-male-speaker-in-wheelchair-on-stage-royalty-free-image/362819531
https://www.picharbor.example/detail/photo/smiling-woman-with-camera-phone-in-dark-audience-royalty-free-image/362818476
https://www.picharbor.example/detail/photo/audience-using-camera-phones-royalty-free-image/367402158
https://www.picharbor.example/detail/photo/male-speaker-on-stage-talking-to-audience-royalty-free-image/362818893

NB: Logos are supplied in low resolution, but I can send you high resolution also
Updates

Hi there I will be adding two low-resolution images of my business partner and I for the ABOUT US page which is called THE BAND in the menu tab.

Hi everyone, thank you for your designs. I have uploaded a MAIN SCREEN IDEAS word document to give you further ideas of how the options I like for the main landing page on the home page. Hope this helps!

Target Market(s)

High end business people in marketing and business.

Coding

Coded - Design and coding required

Number of Pages Required

5+ page

Font styles to use
Sans Serif

Requirements
Must have
• Fresh, inspirational and aspirational designs. We need to make events and conferences look exciting and that we are bring the best technology speakers (like Brightloom events) to our audience of marketing and technology professionals.
Should not have
• Cheesy, old stock photos; or pictures of American executives as this is for an Australian audience.
• PLEASE do not include an UPCOMING EVENTS or a SPEAKERS section as we will not be having this showcasing. You can feature ROCK STARS, LOCAL LEGENDS and UNSUNG HEROES if you like on the home page + the video of YOU and DORIAN PELLHAM (with his picture on the video box with a play button)

```html
<!DOCTYPE html>
<html lang="en">
<head>
<meta charset="utf-8">
<title>Quillfern – Corporate Events &amp; Conferences</title>
<link href="https://fonts.googleapis.com/css2?family=Rajdhani:wght@500;600&family=Roboto:wght@500&display=swap" rel="stylesheet">
<style>
  :root{
    --page:#ffffff;
    --ink:#ffffff;
    --accent:#f26a1b;
    --header:rgba(40,36,36,0.78);
    --btn:rgba(70,50,45,0.82);
  }
  html,body{margin:0;padding:0;}
  body{width:1200px;height:1200px;overflow:hidden;background:var(--page);position:relative;font-family:"Roboto",sans-serif;}
  .site{position:absolute;left:0;top:246px;width:1200px;height:708px;overflow:hidden;}
  .hero-photo{position:absolute;inset:0;
    background:
      radial-gradient(ellipse at 62% 40%, rgba(230,140,60,0.55), transparent 45%),
      linear-gradient(90deg,#2a1d1a 0%,#3b2a22 30%,#6a3e22 55%,#a8a4a8 85%,#c9ccd2 100%);}
  .hero-photo::after{content:"";position:absolute;inset:0;
    background:linear-gradient(180deg,rgba(0,0,0,0.05) 0%,rgba(120,80,50,0.25) 70%,rgba(150,100,60,0.35) 100%);}
  .hero-band{position:absolute;inset:0;}
  .site-header{position:absolute;left:0;top:0;width:1200px;height:92px;background:var(--header);}
  .brand{position:absolute;left:112px;top:18px;display:flex;align-items:center;gap:10px;
    font-family:"Rajdhani",sans-serif;font-weight:600;font-size:46px;color:var(--ink);line-height:1;}
  .brand-dot{width:14px;height:14px;border-radius:50%;background:var(--accent);}
  .main-nav{position:absolute;top:38px;left:0;font-size:13px;color:var(--ink);letter-spacing:0.2px;}
  .main-nav a{position:absolute;white-space:nowrap;color:inherit;text-decoration:none;}
  .main-nav a.is-active::after{content:"";position:absolute;left:0;right:0;top:22px;height:3px;background:var(--accent);}
  .hero-copy{position:absolute;left:0;top:0;width:1200px;text-align:center;color:var(--ink);font-family:"Rajdhani",sans-serif;}
  .hero-kicker{position:absolute;top:266px;width:100%;font-size:21px;font-weight:500;letter-spacing:1.5px;}
  .hero-title{position:absolute;top:300px;width:100%;margin:0;font-size:60px;font-weight:600;line-height:64px;letter-spacing:1px;}
  .hero-rule{position:absolute;left:518px;top:439px;width:164px;height:2px;background:var(--ink);}
  .watch-btn{position:absolute;left:479px;top:462px;width:242px;height:52px;border-radius:26px;background:var(--btn);
    display:flex;align-items:center;justify-content:center;gap:12px;font-size:19px;font-weight:600;letter-spacing:2px;color:var(--ink);}
</style>
</head>
<body>
  <main class="site">
    <div class="hero-photo" role="img" aria-label="Conference audience with a woman standing and asking a question into a microphone, warm orange light and window curtains"></div>
    <svg class="hero-band" width="1200" height="708" viewBox="0 0 1200 708" aria-hidden="true">
      <polygon points="656,0 1048,0 644,708 148,708" fill="#f26a1b" opacity="0.45"/>
      <polygon points="0,0 656,0 148,708 0,708" fill="#1a1210" opacity="0.35"/>
    </svg>

    <header class="site-header">
      <div class="brand"><span class="brand-dot"></span>Quillfern</div>
      <nav class="main-nav">
        <a class="is-active" style="left:401px">HOME</a>
        <a style="left:458px">ROCKSTARS</a>
        <a style="left:552px">LOCAL LEGENDS</a>
        <a style="left:671px">UNSUNG HEROES</a>
        <a style="left:798px">THE BAND</a>
        <a style="left:880px">PARTNERS</a>
        <a style="left:965px">YOU &amp; DORIAN PELLHAM</a>
      </nav>
    </header>

    <section class="hero-copy">
      <div class="hero-kicker">WELCOME TO QUILLFERN</div>
      <h1 class="hero-title">CORPORATE<br>EVENTS &amp; CONFERENCES</h1>
      <div class="hero-rule"></div>
      <div class="watch-btn">
        <svg width="32" height="32" viewBox="0 0 32 32" aria-hidden="true">
          <circle cx="16" cy="16" r="14.5" fill="none" stroke="#fff" stroke-width="1.5"/>
          <polygon points="12.5,9.5 22,16 12.5,22.5" fill="none" stroke="#fff" stroke-width="1.5" stroke-linejoin="round"/>
        </svg>
        WATCH VIDEO
      </div>
    </section>
  </main>
</body>
</html>
```